Brightmoor Pathways

We need a website designed for a life coaching company who specialises in one on one coaching, workshops and seminars where they teach participants in goal setting and how to achieve them for a better life.

Objectives

·         Easy to use

·         Clear & concise

·         Quality but not too flashy

·         Shows clearly what you do and how you interact with clients

·         No fuss, straight up

·         Gives those who hear your name or business name a place to go to obtain further information on what I am doing, why & how they can use my services.

·         A way for clients to contact you

·         Seminar & workshop bookings (not mandatory)

·         Most of the website to be static.

Number of Pages Required

1 page

Requirements
Must have
• Sitemap

• Home
• About Us
• One on One Coaching
• Workshops/Seminars
• How we Work?
• Pricing
• Testimonials
• Contact Us

• Design/Content Brief

• ü  The following elements are included in the design/content brief which this proposal is based on:

• o    Flash banner with some images rotating that reflect your business.

• o    Logo and phone number 0438 760 214 will be prominently displayed.

• o    Horizontal Navigation

• o    Contact Us icon on homepage

• o    Sign up for our newsletter on homepage

• o    Privacy Policy/Sitemap/Terms & Conditions in footer

• o    - larger rounded buttons

• o    - good size font

• o    - not having to scroll too far

• o    - soft feel, but not fluffy (images will enhance this)

• ü  Colours that could be used with logo

• o   What about this?  RGB 128,128,128

• o   What about this?  RGB 54, 95, 145

• o   What about this?  RGB 51, 204, 51

• o   Red – R255

• ü   http://www.plumvexlo.com/

• o    I like this website and its rounded buttons, large easy to see and use.

• o    Soft colours

• o    Changing pictures at the top of screen

• Files

```html
<!DOCTYPE html>
<html lang="en">
<head>
<meta charset="utf-8">
<title>Brightmoor Pathways – Life Coaching</title>
<link href="https://fonts.googleapis.com/css2?family=Montserrat:wght@300;400;500;600&family=Noto+Serif:wght@700&display=swap" rel="stylesheet">
<style>
  :root {
    --page-bg: #dcdde0;
    --card-bg: #ffffff;
    --brand-red: #ee0a0a;
    --btn-red-top: #f23a3a;
    --btn-red-bottom: #c40812;
    --btn-red-edge: #a8060e;
    --grey-top: #d2d3d5;
    --grey-bottom: #8d8e91;
    --text: #111111;
    --footer-grey: #6b6b6b;
    --rule: #848484;
    --placeholder-top: #c4daf2;
    --placeholder-bottom: #dfeaf5;
  }
  * { box-sizing: border-box; margin: 0; padding: 0; }
  html, body { width: 1200px; height: 987px; overflow: hidden; }
  body {
    background: var(--page-bg);
    font-family: "Montserrat", Arial, sans-serif;
    color: var(--text);
    position: relative;
  }
  .site {
    position: absolute; left: 97px; top: -12px; width: 1008px; height: 902px;
    background: var(--card-bg); border-radius: 12px;
    box-shadow: 0 2px 6px rgba(0,0,0,.35);
  }
  .brand { position: absolute; left: 28px; top: 37px; display: flex; align-items: center; gap: 58px; }
  .brand-mark { width: 90px; height: 90px; border-radius: 50%; background: var(--brand-red); }
  .brand-name {
    font-family: "Noto Serif", Georgia, serif; font-weight: 700;
    font-size: 29px; color: var(--brand-red);
  }
  .phone {
    position: absolute; left: 773px; top: 0; width: 195px; height: 73px;
    border-radius: 0 0 6px 6px;
    background: linear-gradient(var(--grey-top), var(--grey-bottom));
    color: #fff; text-align: center; padding-top: 17px;
  }
  .phone-label { font-size: 19px; line-height: 20px; font-weight: 400; }
  .phone-number { font-size: 24px; line-height: 28px; font-weight: 600; letter-spacing: .5px; }
  .banner {
    position: absolute; left: 13px; top: 134px; width: 982px; height: 188px;
    border-radius: 12px; overflow: hidden;
  }
  .banner-photo {
    position: absolute; inset: 0;
    background: linear-gradient(var(--placeholder-top), var(--placeholder-bottom));
  }
  .banner-tagline {
    position: absolute; right: 33px; top: 72px;
    font-size: 31px; font-weight: 400; color: var(--text); letter-spacing: .2px;
  }
  .main-nav { position: absolute; left: 13px; top: 335px; display: flex; gap: 13px; }
  .main-nav a {
    width: 153px; height: 62px; border-radius: 6px;
    background: linear-gradient(var(--btn-red-top), var(--btn-red-bottom));
    border: 2px solid var(--btn-red-edge);
    color: #fff; text-decoration: none; font-size: 17px; line-height: 17px;
    display: flex; align-items: center; justify-content: center; text-align: center;
    position: relative; overflow: hidden;
  }
  .main-nav a::before {
    content: ""; position: absolute; left: -10px; right: -10px; top: -30px; height: 52px;
    border-radius: 50%; background: rgba(255,255,255,.18);
  }
  .main-nav a span { position: relative; }
  .intro { position: absolute; left: 40px; top: 431px; width: 692px; }
  .intro h1 {
    font-size: 39.5px; line-height: 42px; font-weight: 300; color: var(--brand-red);
    margin-bottom: 14px;
  }
  .intro h1 strong { font-weight: 600; }
  .intro p { font-size: 19px; line-height: 26px; text-align: justify; margin-bottom: 26px; }
  .side { position: absolute; left: 773px; width: 195px; text-align: center; color: var(--text); text-decoration: none; }
  .side-label { font-size: 17px; line-height: 18px; font-weight: 500; display: block; }
  .contact { top: 444px; }
  .newsletter { top: 566px; }
  .side svg { display: block; margin: 0 auto 12px; }
  .join {
    position: absolute; left: 773px; top: 743px; width: 195px; height: 68px;
    border-radius: 6px; border: 2px solid var(--btn-red-edge);
    background: linear-gradient(var(--btn-red-top), var(--btn-red-bottom));
    color: #fff; text-align: center; text-decoration: none; padding-top: 10px;
  }
  .join-main { display: block; font-size: 24px; line-height: 26px; font-weight: 500; }
  .join-sub { display: block; font-size: 15px; line-height: 17px; }
  .site-footer {
    position: absolute; left: 13px; top: 857px; width: 982px;
    border-top: 2px solid var(--rule); padding-top: 13px;
    display: flex; justify-content: space-between; font-size: 15px; font-weight: 500;
  }
  .copyright { color: var(--brand-red); margin-left: -1px; }
  .legal a { color: var(--footer-grey); text-decoration: none; }
  .legal .sep { color: var(--footer-grey); margin: 0 8px; }
</style>
</head>
<body>
<div class="site">
  <header>
    <div class="brand">
      <span class="brand-mark"></span>
      <span class="brand-name">Brightmoor Pathways</span>
    </div>
    <div class="phone">
      <div class="phone-label">Call us on</div>
      <div class="phone-number">0438 760 214</div>
    </div>
  </header>

  <section class="banner">
    <div class="banner-photo" role="img" aria-label="Banner photo placeholder: a person relaxing outdoors"></div>
    <p class="banner-tagline">Access your potential and achieve your success</p>
  </section>

  <nav class="main-nav">
    <a href="#"><span>Your Coach</span></a>
    <a href="#"><span>Services<br>Available</span></a>
    <a href="#"><span>Coaching</span></a>
    <a href="#"><span>Workshops &amp;<br>Seminars</span></a>
    <a href="#"><span>Your<br>Investment</span></a>
    <a href="#"><span>Testimonials</span></a>
  </nav>

  <main class="intro">
    <h1>We help you <strong>set positive goals</strong> to help better your life.</h1>
    <p>Lorem ipsum dolor sit amet, consectetur adipiscing elit. Fusce volutpat pulvinar enim. Praesent sit amet nisi metus. In hac habitasse platea dictumst. Ut sodales erat ac sem mattis vel mollis erat blandit. Donec convallis porttitor nunc, sed euismod nisl consequat non.</p>
    <p>Ut nec mauris ante. Suspendisse potenti. Class aptent taciti sociosqu ad litora torquent per conubia nostra, per inceptos himenaeos.</p>
    <p>Aliquam eu ipsum metus, a porta tellus. Duis tellus risus, dignissim et porttitor quis, pretium fermentum nisi. Aliquam erat volutpat. Quisque quam neque, dapibus in malesuada at, congue vitae ipsum.</p>
  </main>

  <a class="side contact" href="#">
    <svg width="78" height="42" viewBox="0 0 78 42">
      <defs><linearGradient id="env" x1="0" y1="0" x2="0" y2="1"><stop offset="0" stop-color="#f44"/><stop offset="1" stop-color="#c40812"/></linearGradient></defs>
      <rect x="1" y="1" width="76" height="40" rx="3" fill="url(#env)" stroke="#a8060e"/>
      <path d="M3 4 L39 26 L75 4" fill="none" stroke="#fff" stroke-width="2.5"/>
      <path d="M3 39 L30 20 M75 39 L48 20" fill="none" stroke="#fff" stroke-width="2"/>
    </svg>
    <span class="side-label">Contact Us</span>
  </a>

  <a class="side newsletter" href="#">
    <svg width="78" height="84" viewBox="0 0 78 84">
      <defs><linearGradient id="doc" x1="0" y1="0" x2="0" y2="1"><stop offset="0" stop-color="#f44"/><stop offset="1" stop-color="#c40812"/></linearGradient></defs>
      <rect x="1" y="1" width="76" height="82" rx="4" fill="url(#doc)" stroke="#a8060e"/>
      <g stroke="#fff" stroke-width="2.5">
        <line x1="8" y1="14" x2="48" y2="14"/><line x1="8" y1="24" x2="68" y2="24"/>
        <line x1="8" y1="34" x2="64" y2="34"/><line x1="8" y1="44" x2="48" y2="44"/>
        <line x1="8" y1="54" x2="68" y2="54"/><line x1="8" y1="64" x2="68" y2="64"/>
        <line x1="8" y1="74" x2="38" y2="74"/>
      </g>
    </svg>
    <span class="side-label">Sign up for<br>our newsletter</span>
  </a>

  <a class="join" href="#">
    <span class="join-main">Join us at our</span>
    <span class="join-sub">Workshops &amp; Seminars</span>
  </a>

  <footer class="site-footer">
    <span class="copyright">©2009 Brightmoor Pathways</span>
    <span class="legal"><a href="#">Privacy Policy</a><span class="sep">|</span><a href="#">Sitemap</a><span class="sep">|</span><a href="#">Terms &amp; Conditions</a></span>
  </footer>
</div>
</body>
</html>
```